Need App for Impact Related Events

My app is to help with internal events. When you enter the prompted event code the next screen shows you everyone currently at the event. It will give you the ability to Start a conversation with someone you met at that event, or signal it is your turn to send a message. The next screen is a message thread with that person. I am looking for a design that incorporates the colors and ‘feel good’ emotion of our logo. I have pieced together a pretty good interpretation of what I’m looking for in the attached mockup by slicing and dicing designs. I also attached our logo mascot.Screens (see attached mockups)

Note 1: I do not like the picture on the screen used in screen one because it makes it seem like a dating app. I attached an alternative photo that can be used or present different ideas.

Note 2: On the login/signup screen (screen 2) I need an additional first and last name for login, you can try to fit this on one login screen or present a two step signup screen where that is presented in the second screen.

READ MOCKUP GUIDELINES UNDER Must Haves

Target Market(s)

People attending internal social impact events

Industry/Entity Type

Charity

Font styles to use
Sans Serif

Colors
86cfc6

Requirements
Must have
• Follow the screen mockups attached to project
• PLEASE READ
• I have provided a relatively close design of what I’m looking for in the mockups. Some screens need to be followed more closely to my design mockup than other. I have listed a guide below how how closely you should follow my mockup design exactly. Overall I would like to see some ideas of incorporating a few accent colors so it doesn’t appear SO Blue. I also attached some app inspiration designs I found from around the web
• Screen Mockup Guideline Follow %
• Screen 1: 65% - mostly on target, would like to see ways to make it not SO Blue and possibly creative places to add some explainer text describing the app
• Screen 2: 50% - general design idea is here, but more open
• Screen 3: 35% - a lot more room for design influence
• Screen 4: 70% - mostly on target, a little room for design influence/color scheme ideas
• Screen 5-6: 25% - a lot of room for design change/ideas/influence
• Screen 7-8: 80% - already very close to what I need, maybe open to slight sizing and color scheme ideas
• Screen 9: 15% - the most open for influence, only the general functionality of the screen is communicated here
Nice to have
• Please Read Mockup Guideline above. In large part I am looking for something to use some nice accent colors so it is not overwhelmingly blue and bring the whole design into a seamless style.
Should not have

```html
<!DOCTYPE html>
<html lang="en">
<head>
<meta charset="utf-8">
<title>Kindly – App Screens</title>
<link rel="stylesheet" href="https://fonts.googleapis.com/css2?family=Questrial&family=Lato:wght@400;700&display=swap">
<style>
:root{
  --cyan:#1ed9ec;
  --sky:#c4f1f9;
  --sky-pale:#e3f8fb;
  --cream:#fcf7f3;
  --peach:#fde3d6;
  --coral:#ff8a73;
  --sun:#ffd27a;
  --ink:#2a2a2a;
  --grey:#9b9b9b;
  --grey-line:#c9c9c9;
  --slate:#666a6c;
  --white:#ffffff;
}
*{margin:0;padding:0;box-sizing:border-box}
html,body{width:1200px;height:768px;overflow:hidden}
body{background:var(--white);font-family:"Questrial",sans-serif;color:var(--ink);position:relative}
.screen{position:absolute;overflow:hidden;background:var(--cream);box-shadow:0 0 28px rgba(120,225,240,.35)}
.abs{position:absolute}
.status{position:absolute;top:0;left:0;right:0;height:16px;font-family:"Lato",sans-serif;font-size:8px;color:var(--ink);z-index:2}
.status .signal{position:absolute;left:8px;top:5px;width:18px;height:6px}
.status .time{position:absolute;left:0;right:0;top:4px;text-align:center}
.status .battery{position:absolute;right:8px;top:4px;display:flex;align-items:center;gap:3px}
.status .battery i{display:inline-block;width:16px;height:6px;border:1px solid currentColor;border-radius:1px;position:relative}
.status .battery i::after{content:"";position:absolute;inset:1px;background:currentColor}
.status.light{color:var(--white)}
.brand{position:absolute;left:0;right:0;display:flex;justify-content:center;align-items:center;gap:4px;font-size:13px;color:var(--ink)}
.brand .mark{width:8px;height:8px;border-radius:50%;background:var(--coral)}
.brand.small{font-size:9px}
.brand.small .mark{width:5px;height:5px}
.btn{position:absolute;left:50%;transform:translateX(-50%);height:30px;border-radius:15px;background:var(--cyan);color:var(--white);font-size:10px;display:flex;align-items:center;justify-content:center}
.btn.accent{background:var(--coral)}
.link{position:absolute;left:0;right:0;text-align:center;font-size:9.5px;color:var(--cyan);text-decoration:underline}
.field{position:absolute;border-bottom:1px solid var(--grey-line);text-align:center;font-family:"Lato",sans-serif;font-size:8.5px;color:var(--grey);padding-bottom:6px}
.field.wide{left:50%;transform:translateX(-50%)}
.title{position:absolute;left:0;right:0;text-align:center;color:var(--ink)}
.gear{position:absolute;width:11px;height:11px}
.back{position:absolute;width:12px;height:10px}
.deco{position:absolute;left:0;top:0}
.photo{position:absolute}
.avatar{position:absolute;border-radius:50%}
.header{position:absolute;left:0;right:0;top:0;background:var(--cream)}
.body-white{background:var(--white)}
.muted{font-family:"Lato",sans-serif;color:var(--grey)}
.contact{position:absolute;left:0;right:0;height:52px}
.contact .name{position:absolute;left:77px;top:-9px;font-size:11.5px;color:var(--ink)}
.contact .msg{position:absolute;left:77px;top:8px;font-family:"Lato",sans-serif;font-size:7.5px;color:#b5b5b5}
.contact .msg.unread{color:var(--ink)}
.contact .when{position:absolute;right:26px;top:-5px;font-family:"Lato",sans-serif;font-size:8px;font-weight:700}
.contact .online{display:inline-block;width:5px;height:5px;border-radius:50%;background:var(--coral);margin-left:5px;vertical-align:middle}
.bubble{position:absolute;background:var(--cyan);color:var(--white);font-family:"Lato",sans-serif;font-size:8.5px;border-radius:13px;padding:0 15px;display:flex;align-items:center;line-height:1.4}
.bubble.accent{background:var(--coral)}
</style>
</head>
<body>

<svg width="0" height="0" style="position:absolute">
  <defs>
    <path id="cog" d="M19.4 13a7.7 7.7 0 0 0 0-2l2.1-1.6-2-3.5-2.5 1a7.6 7.6 0 0 0-1.7-1L15 3h-4l-.4 2.9a7.6 7.6 0 0 0-1.7 1l-2.5-1-2 3.5L6.6 11a7.7 7.7 0 0 0 0 2l-2.1 1.6 2 3.5 2.5-1a7.6 7.6 0 0 0 1.7 1L11 21h4l.4-2.9a7.6 7.6 0 0 0 1.7-1l2.5 1 2-3.5zM13 15.5a3.5 3.5 0 1 1 0-7 3.5 3.5 0 0 1 0 7z"/>
    <g id="bars"><rect x="0" y="4" width="2" height="2"/><rect x="3" y="2.5" width="2" height="3.5"/><rect x="6" y="1" width="2" height="5"/><rect x="9" y="0" width="2" height="6"/></g>
  </defs>
</svg>

<!-- Welcome -->
<section class="screen welcome" style="left:40px;top:14px;width:255px;height:454px;background:linear-gradient(180deg,var(--sky) 45%,var(--sky-pale) 75%,var(--peach) 100%)">
  <div class="photo" role="img" aria-label="Photo of two smiling friends at a café event" style="left:0;top:0;width:255px;height:240px;background:linear-gradient(160deg,#c9c6c0 0%,#8f8a84 40%,#5b524c 70%,#3d3531 100%)"></div>
  <svg class="deco" width="255" height="454" viewBox="0 0 255 454">
    <path d="M0 175 C40 170 60 205 110 205 C150 205 170 190 200 215 C225 235 240 225 255 215 L255 454 L0 454 Z" fill="#c6f1f9"/>
    <path d="M0 400 C60 370 120 430 255 380 L255 454 L0 454 Z" fill="var(--peach)"/>
    <path d="M0 425 C80 405 150 450 255 420 L255 454 L0 454 Z" fill="var(--sun)" opacity=".45"/>
  </svg>
  <div class="status light"><svg class="signal" viewBox="0 0 18 6" fill="#fff"><use href="#bars"/></svg><span class="time">9:41 AM</span><span class="battery">100% <i></i></span></div>
  <div class="brand" style="top:228px">Kindly <span class="mark"></span></div>
  <div class="title" style="top:261px;font-size:10px;font-family:'Lato',sans-serif;font-weight:700">Be Nice. Be Kind.</div>
  <div class="btn" style="top:312px;width:86px">Sign In</div>
  <div class="btn accent" style="top:356px;width:86px">Sign Up</div>
</section>

<!-- Sign in -->
<section class="screen sign-in" style="left:334px;top:0;width:256px;height:364px;background:linear-gradient(180deg,var(--sky) 0%,var(--sky) 50%,var(--sky-pale) 75%,var(--peach) 100%)">
  <div class="photo" role="img" aria-label="Photo of a smiling person at an event" style="left:0;top:0;width:256px;height:120px;background:linear-gradient(150deg,#d9cfc6 0%,#a98f7e 40%,#5e4a40 100%)"></div>
  <svg class="deco" width="256" height="364" viewBox="0 0 256 364">
    <path d="M0 95 C60 100 90 125 140 90 C175 65 200 30 256 20 L256 364 L0 364 Z" fill="#c6f1f9"/>
    <path d="M0 335 C70 310 150 360 256 320 L256 364 L0 364 Z" fill="var(--peach)"/>
  </svg>
  <div class="title" style="top:118px;font-size:17px">Sign In</div>
  <div class="field" style="left:65px;top:158px;width:58px">First name</div>
  <div class="field" style="left:133px;top:158px;width:58px">Last name</div>
  <div class="field wide" style="top:190px;width:125px">Email</div>
  <div class="field wide" style="top:222px;width:125px">Password</div>
  <div class="btn" style="top:257px;width:86px">Take Me In</div>
  <div class="link" style="top:299px">I don't have an account</div>
</section>

<!-- Location code -->
<section class="screen location-code" style="left:611px;top:0;width:259px;height:446px">
  <svg class="deco" width="259" height="446" viewBox="0 0 259 446">
    <path d="M0 330 C40 345 70 360 110 340 C160 315 200 280 259 255 L259 446 L0 446 Z" fill="#bdeff9"/>
    <path d="M0 405 C70 380 160 430 259 395 L259 446 L0 446 Z" fill="var(--peach)"/>
  </svg>
  <svg class="gear" style="left:225px;top:32px" viewBox="0 0 24 24" fill="#222"><use href="#cog"/></svg>
  <div class="brand" style="top:104px">Kindly <span class="mark"></span></div>
  <div class="title" style="top:146px;font-size:17.5px">Location Kind Code</div>
  <div class="field wide" style="top:201px;width:126px">Type Here</div>
  <div class="btn" style="top:254px;width:86px">Enter Code</div>
  <div class="link" style="top:299px">Create Your Own Code</div>
</section>

<!-- Your code -->
<section class="screen your-code" style="left:895px;top:0;width:261px;height:448px">
  <svg class="deco" width="261" height="448" viewBox="0 0 261 448">
    <path d="M0 275 C30 285 60 330 100 345 C150 360 200 325 261 315 L261 448 L0 448 Z" fill="#bdeff9"/>
    <path d="M0 410 C80 385 170 435 261 400 L261 448 L0 448 Z" fill="var(--peach)"/>
  </svg>
  <svg class="gear" style="left:227px;top:33px" viewBox="0 0 24 24" fill="#222"><use href="#cog"/></svg>
  <div class="brand" style="top:106px">Kindly <span class="mark"></span></div>
  <div class="title" style="top:148px;font-size:17.5px">Your Code</div>
  <div class="title" style="top:180px;font-size:23px;color:var(--coral)">AF45922JB38</div>
  <div class="title muted" style="top:221px;font-size:8.5px;line-height:12px">Give this code to the people<br>at your location or event to allow<br>them to connect to each other.</div>
  <div class="title muted" style="top:269px;font-size:8.5px">Like a wifi password.</div>
  <div class="btn" style="top:301px;width:86px">Copy</div>
  <div class="link" style="top:347px">Manage in Settings</div>
</section>

<!-- Settings -->
<section class="screen settings body-white" style="left:43px;top:489px;width:239px;height:279px">
  <div class="header" style="height:183px"></div>
  <div class="status"><svg class="signal" viewBox="0 0 18 6" fill="#222"><use href="#bars"/></svg><span class="time">9:41 AM</span><span class="battery">100% <i></i></span></div>
  <div class="brand small" style="top:24px">Kindly <span class="mark"></span></div>
  <div class="title" style="top:43px;font-size:9.5px">Settings</div>
  <svg class="back" style="left:21px;top:44px" viewBox="0 0 12 10"><path d="M11 5H2M5.5 1 1.5 5l4 4" stroke="#222" stroke-width="1.6" fill="none"/></svg>
  <div class="avatar" role="img" aria-label="Profile photo of the user" style="left:85px;top:65px;width:68px;height:68px;background:linear-gradient(160deg,#e8e6e2,#9b9a95 60%,#4f4d4a)"></div>
  <div class="avatar" style="left:110px;top:123px;width:18px;height:18px;background:#fff;display:flex;align-items:center;justify-content:center;box-shadow:0 1px 3px rgba(0,0,0,.15)"><svg width="9" height="7" viewBox="0 0 9 7"><rect x="0" y="1.3" width="9" height="5.7" rx="1" fill="#222"/><rect x="3" y="0" width="3" height="2" fill="#222"/><circle cx="4.5" cy="4" r="1.5" fill="#fff"/></svg></div>
  <div class="abs" style="left:81px;top:161px;font-size:9px">My Info</div>
  <div class="abs" style="left:80px;top:176px;width:37px;height:2px;background:var(--cyan)"></div>
  <div class="abs" style="left:142px;top:161px;font-size:9px">Events</div>
  <div class="abs" style="left:178px;top:157px;width:4px;height:4px;border-radius:50%;background:var(--coral)"></div>
  <div class="abs muted" style="left:23px;top:211px;font-size:7px">Sept 19</div>
  <div class="abs" style="left:23px;top:226px;font-size:10px;font-family:'Lato',sans-serif">A12TM326621</div>
  <div class="abs muted" style="left:110px;top:227px;font-size:8px;color:#c0c0c0">Swipe to delete tap to edit</div>
  <div class="abs muted" style="left:23px;top:261px;font-size:7px">Sept 15</div>
</section>

<!-- Profile photo -->
<section class="screen profile-photo body-white" style="left:333px;top:400px;width:252px;height:368px">
  <svg class="deco" width="252" height="368" viewBox="0 0 252 368">
    <path d="M0 205 C30 210 50 240 85 260 C130 285 190 255 252 230 L252 368 L0 368 Z" fill="#c6f1f9"/>
    <path d="M0 340 C70 315 160 365 252 330 L252 368 L0 368 Z" fill="var(--peach)"/>
  </svg>
  <div class="status"><svg class="signal" viewBox="0 0 18 6" fill="#222"><use href="#bars"/></svg><span class="time">9:41 AM</span><span class="battery">100% <i></i></span></div>
  <div class="avatar" role="img" aria-label="Blurred placeholder profile photo" style="left:54px;top:92px;width:144px;height:144px;background:radial-gradient(circle at 50% 40%,#a9a9a9 0%,#c9c9c9 35%,#efefef 70%,#f7f7f7 100%)"></div>
  <svg class="abs" style="left:113px;top:152px" width="26" height="21" viewBox="0 0 26 21"><rect x="0" y="4" width="26" height="17" rx="3" fill="#6f6f6f"/><rect x="8" y="0" width="10" height="6" rx="1.5" fill="#6f6f6f"/><circle cx="13" cy="12.5" r="5" fill="#d8d8d8"/><circle cx="13" cy="12.5" r="3" fill="#6f6f6f"/></svg>
  <div class="btn" style="top:261px;width:84px">Use this</div>
  <div class="link" style="top:305px">Skip for now</div>
</section>

<!-- Contacts -->
<section class="screen contacts body-white" style="left:606px;top:466px;width:268px;height:302px">
  <div class="header" style="height:76px;box-shadow:0 3px 8px rgba(0,0,0,.04)"></div>
  <div class="status"><svg class="signal" viewBox="0 0 18 6" fill="#222"><use href="#bars"/></svg><span class="time">9:41 AM</span><span class="battery">100% <i></i></span></div>
  <div class="brand small" style="top:28px">Kindly <span class="mark"></span></div>
  <div class="title" style="top:48px;font-size:10px">Who you've met so far</div>
  <svg class="back" style="left:23px;top:49px" viewBox="0 0 12 10"><path d="M11 5H2M5.5 1 1.5 5l4 4" stroke="#222" stroke-width="1.6" fill="none"/></svg>
  <svg class="gear" style="left:236px;top:49px" viewBox="0 0 24 24" fill="#222"><use href="#cog"/></svg>

  <div class="contact" style="top:122px">
    <div class="avatar" role="img" aria-label="Profile photo of Mara Ellison" style="left:26px;top:-19px;width:38px;height:38px;background:linear-gradient(150deg,#f3c9bd,#c98572)"></div>
    <span class="name">Mara Ellison</span><span class="msg">Nice to meeting you too</span><span class="when">1m</span>
  </div>
  <div class="contact" style="top:174px">
    <div class="avatar" role="img" aria-label="Profile photo of Lucia Navarro" style="left:26px;top:-19px;width:38px;height:38px;background:linear-gradient(150deg,#d7b3a5,#6b4538)"></div>
    <span class="name">Lucia Navarro</span><span class="msg">Yeah Cool!</span><span class="when">24m</span>
  </div>
  <div class="contact" style="top:226px">
    <div class="avatar" role="img" aria-label="Profile photo of Ivy Thornwell" style="left:26px;top:-19px;width:38px;height:38px;background:linear-gradient(150deg,#cfd2d4,#5a5654)"></div>
    <span class="name">Ivy Thornwell<span class="online"></span></span><span class="msg unread">You were at the parking lot..</span><span class="when">56m</span>
  </div>
  <div class="contact" style="top:278px">
    <div class="avatar" role="img" aria-label="Profile photo of Nadia Rowe" style="left:26px;top:-19px;width:38px;height:38px;background:linear-gradient(150deg,#e7c6b3,#b37d63)"></div>
    <span class="name">Nadia Rowe</span><span class="msg">Nice to meeting you too</span><span class="when">1hr</span>
  </div>
</section>

<!-- Chat thread -->
<section class="screen chat body-white" style="left:898px;top:491px;width:253px;height:277px">
  <div class="header" style="height:71px;box-shadow:0 3px 8px rgba(0,0,0,.04)"></div>
  <div class="status"><svg class="signal" viewBox="0 0 18 6" fill="#222"><use href="#bars"/></svg><span class="time">9:41 AM</span><span class="battery">100% <i></i></span></div>
  <div class="avatar" role="img" aria-label="Profile photo of Mara Ellison" style="left:117px;top:21px;width:20px;height:20px;background:linear-gradient(150deg,#f3c9bd,#c98572)"></div>
  <div class="title" style="top:46px;font-size:10px">Mara Ellison</div>
  <svg class="back" style="left:22px;top:47px" viewBox="0 0 12 10"><path d="M11 5H2M5.5 1 1.5 5l4 4" stroke="#222" stroke-width="1.6" fill="none"/></svg>
  <svg class="gear" style="left:221px;top:46px" viewBox="0 0 24 24" fill="#222"><use href="#cog"/></svg>
  <div class="bubble" style="left:55px;top:170px;height:26px;padding:0 11px">Hi there!</div>
  <div class="bubble" style="left:55px;top:201px;width:156px;height:42px;padding:0 15px">You've got some great<br>recommendations from us</div>
  <div class="avatar" role="img" aria-label="Profile photo of Mara Ellison" style="left:26px;top:247px;width:22px;height:22px;background:linear-gradient(150deg,#f3c9bd,#c98572)"></div>
  <div class="bubble accent" style="left:55px;top:249px;width:109px;height:28px">Nice meeting you!</div>
</section>

</body>
</html>
```